The Brambury Firm

We need a new design for our letterhead and envelopes. We are a personal injury and criminal defense firm so we need something modern and clean, but more on the professional/traditional side. Our new logo has two colors and is attached to the file so we need something that works well with those colors/matches the design. The following information needs to be on the letterhead:
Phone: (555) 314-7265
Fax: (555) 419-6032
Toll-Free: (555) 736-1149
Post Office Box 4273
Lexington, SC 29458-4273
TQHarmClaimsDesk.example
PalmettoShieldCounsel.example

Target Market(s)

Clients, government agencies, other law firms

Industry/Entity Type

Legal

Font styles to use
Sans Serif
Other font styles liked:
• Arial

Colors

Designer to choose colors to be used in the design.

Requirements
Must have
• Must look professional and clean, modern
Nice to have
• I would like to see a design that works with the logo but does not distract from the content that will be printed on it
Should not have
• Too many colors or crazy designs.

```html
<!DOCTYPE html>
<html lang="en">
<head>
<meta charset="utf-8">
<title>The Brambury Firm – Stationery</title>
<link href="https://fonts.googleapis.com/css2?family=EB+Garamond:wght@500&family=Work+Sans:wght@400;500&display=swap" rel="stylesheet">
<style>
  :root {
    --navy: #262c8c;
    --navy-deep: #242b86;
    --red: #d9232b;
    --ink: #1d2a55;
    --paper: #ffffff;
    --backdrop: #eceae6;
    --flap: #e3e3e3;
  }
  * { margin: 0; padding: 0; box-sizing: border-box; }
  html, body { width: 1200px; height: 849px; overflow: hidden; }
  body { background: var(--backdrop); position: relative; font-family: "Work Sans", Arial, sans-serif; color: var(--ink); }

  .sheet { position: absolute; background: var(--paper); box-shadow: 0 2px 6px rgba(0,0,0,.18); overflow: hidden; }
  .letterhead { left: 106px; top: 95px; width: 468px; height: 657px; }
  .envelope-front { left: 614px; top: 112px; width: 475px; height: 237px; }
  .envelope-back { left: 610px; top: 389px; width: 478px; height: 335px; background: none; box-shadow: 0 2px 6px rgba(0,0,0,.2); }

  .firm-name { position: absolute; display: flex; align-items: center; gap: 7px;
    font-family: "EB Garamond", Georgia, serif; font-weight: 500; color: var(--navy); white-space: nowrap; }
  .firm-name .mark { width: 10px; height: 10px; background: var(--red); flex: none; }
  .letterhead .firm-name { left: 50px; top: 72px; font-size: 21px; }
  .envelope-front .firm-name { left: 27px; top: 131px; font-size: 18px; }

  .contact { position: absolute; left: 285px; top: 46px; font-size: 7.4px; line-height: 10px; letter-spacing: .3px; }
  .contact li { list-style: none; display: flex; align-items: center; gap: 6px; }
  .contact svg { width: 7px; height: 7px; fill: var(--navy); flex: none; }
  .address { font-size: 7.4px; line-height: 9.6px; letter-spacing: .3px; }
  .address .web { margin-top: 2px; }
  .letterhead .address { position: absolute; left: 285px; top: 92px; }
  .envelope-front .address { position: absolute; left: 27px; top: 187px; }

  .greeting { position: absolute; left: 49px; top: 219px; font-family: "EB Garamond", Georgia, serif;
    font-weight: 500; font-size: 18px; color: var(--navy); letter-spacing: .3px; }
  .body-copy { position: absolute; left: 49px; top: 260px; width: 356px; font-size: 7.3px; line-height: 12.3px; letter-spacing: .25px; }
  .body-copy p + p { margin-top: 9px; }
  .sign-name { position: absolute; left: 49px; top: 477px; font-family: "EB Garamond", Georgia, serif; font-size: 13px; color: var(--ink); }
  .signature { position: absolute; left: 44px; top: 508px; width: 102px; height: 22px; background: linear-gradient(90deg, #e4e6f2, #f1f2f8); border-radius: 3px; }

  .band { position: absolute; left: 0; bottom: 0; width: 100%; height: 10px; }
  .envelope-front .band { height: 8px; }
  .envelope-back svg { display: block; }
</style>
</head>
<body>

<section class="sheet letterhead">
  <div class="firm-name"><span class="mark"></span>The Brambury Firm</div>

  <ul class="contact">
    <li><svg viewBox="0 0 10 10"><rect x="2.5" y="0" width="5" height="10" rx="1"/></svg>(555) 314-7265</li>
    <li><svg viewBox="0 0 10 10"><rect x="1" y="3" width="8" height="5"/><rect x="3" y="0" width="4" height="3"/></svg>(555) 419-6032</li>
    <li><svg viewBox="0 0 10 10"><path d="M2 0l2 2-1 2c1 2 2 3 3 3l2-1 2 2-1 2C4 10 0 6 0 2z"/></svg>(555) 736-1149 (Toll-Free)</li>
    <li><svg viewBox="0 0 10 10"><circle cx="5" cy="5" r="4.5" fill="none" stroke="#262c8c" stroke-width="1"/><path d="M0.5 5h9M5 .5v9" stroke="#262c8c" stroke-width=".8"/></svg>TQHarmClaimsDesk.example</li>
  </ul>

  <div class="address">
    <div>Post Office Box 4273</div>
    <div>Lexington, SC 29458-4273</div>
    <div class="web">PalmettoShieldCounsel.example</div>
  </div>

  <h1 class="greeting">Hello Carter,</h1>

  <div class="body-copy">
    <p>Lorem ipsum dolor sit amet, consectetur adipisicing elit, sed do eiusmod tempor incididunt ut labore et dolore magna aliqua. Ut enim ad minim veniam, quis nostrud exercitation ullamco laboris nisi ut aliquip ex ea commodo consequat. Duis aute irure dolor in reprehenderit in voluptate velit esse cillum dolore eu fugiat nulla pariatur. Excepteur sint occaecat cupidatat non proident, sunt in culpa qui officia deserunt mollit anim id est laborum. Sed ut perspiciatis unde omnis iste natus error sit voluptatem accusantium doloremque laudantium.</p>
    <p>Lorem ipsum dolor sit amet, consectetur adipisicing elit, sed do eiusmod tempor incididunt ut labore et dolore magna aliqua. Ut enim ad minim veniam, quis nostrud exercitation ullamco laboris nisi ut aliquip ex ea commodo consequat.</p>
    <p>Lorem ipsum dolor sit amet, consectetur adipisicing elit, sed do eiusmod tempor incididunt ut labore et dolore magna aliqua.</p>
  </div>

  <div class="sign-name">Marcus Hale</div>
  <div class="signature" role="img" aria-label="Handwritten signature of Marcus Hale"></div>

  <svg class="band" viewBox="0 0 468 10" preserveAspectRatio="none">
    <polygon points="0,0 232,0 228,10 0,10" fill="var(--navy)"/>
    <polygon points="240,0 468,0 468,10 236,10" fill="var(--red)"/>
  </svg>
</section>

<section class="sheet envelope-front">
  <div class="firm-name"><span class="mark"></span>The Brambury Firm</div>
  <div class="address">
    <div>Post Office Box 4273</div>
    <div>Lexington, SC 29458-4273</div>
    <div class="web">PalmettoShieldCounsel.example</div>
  </div>
  <svg class="band" viewBox="0 0 475 8" preserveAspectRatio="none">
    <polygon points="0,0 234,0 230,8 0,8" fill="var(--navy)"/>
    <polygon points="242,0 475,0 475,8 238,8" fill="var(--red)"/>
  </svg>
</section>

<section class="sheet envelope-back">
  <svg width="478" height="335" viewBox="0 0 478 335">
    <defs>
      <linearGradient id="flapShade" x1="0" y1="0" x2="0" y2="1">
        <stop offset="0" stop-color="#f2f2f2"/>
        <stop offset="1" stop-color="#d9d9d9"/>
      </linearGradient>
    </defs>
    <path d="M30 0H446Q454 0 456 8L478 112H0L22 8Q24 0 30 0Z" fill="url(#flapShade)"/>
    <rect x="0" y="112" width="478" height="223" fill="var(--navy)"/>
    <polygon points="0,112 30,170 34,335 0,335" fill="#22297f"/>
    <polygon points="478,112 448,170 444,335 478,335" fill="#22297f"/>
    <path d="M34 166Q34 163 38 163H440Q444 163 444 166V335H34Z" fill="var(--navy-deep)"/>
    <polygon points="0,112 478,112 448,170 30,170" fill="#ececec"/>
    <text x="239" y="262" text-anchor="middle" font-family="EB Garamond, Georgia, serif" font-weight="500" font-size="15" fill="#ffffff">The Brambury Firm</text>
  </svg>
</section>

</body>
</html>
```